Business card design needed

We are 2 artists starting up a studio by the water in Sydney ...where we can work and display our art...would like the back ground to be Navy and white stripe...nautical...and the name The Paint Hut to be bold and the main wording...not nautical...if possible thought the A for art could be an easel ...ie the capital A using the cross bar as the platform that paint would be circles of colour....would like the main wording in Black but the easel A in colour
Hope u are able to help
thanku Lorna Vesk
as I will be away in a week for 4 weeks could u please send all info to Mira Colbins email....she can contact me and we can go ahead asap....

Artists

THE PAINT HUT

Hallorans Oar House
The Reach..17 Kellaby Rd..Dunrook 2091 Sydney

Mir Colbin..0437819025..miracolbin@mailnest.example
Lorn Vesk...0429573816..lvesk@harborlink.example

```html
<!DOCTYPE html>
<html lang="en">
<head>
<meta charset="utf-8">
<title>The Paint Hut – Business Card</title>
<link rel="stylesheet" href="https://fonts.googleapis.com/css2?family=Roboto:wght@400;700&display=swap">
<style>
  :root {
    --card-bg: #ffffff;
    --wave-tone: #a9dcf3;
    --wave-tone-soft: #d6eefa;
    --ink: #333333;
    --name-ink: #2e2e2e;
    --frame: #d9d9d9;
    --rule: #e2e2e2;
  }
  html, body {
    margin: 0;
    padding: 0;
    overflow: hidden;
    background: var(--card-bg);
  }
  .card {
    position: relative;
    width: 1200px;
    height: 677px;
    overflow: hidden;
    background: var(--card-bg);
    border: 1px solid var(--frame);
    box-sizing: border-box;
    font-family: "Roboto", Arial, sans-serif;
    color: var(--ink);
  }
  .wave-field {
    position: absolute;
    inset: 0;
    background: linear-gradient(160deg, var(--wave-tone-soft) 0%, #eaf6fc 50%, var(--wave-tone-soft) 100%);
  }
  .brand {
    position: absolute;
    left: 0;
    right: 0;
    top: 170px;
    text-align: center;
  }
  .brand-name {
    margin: 0;
    font-family: "Roboto", Arial, sans-serif;
    font-weight: 700;
    font-size: 118px;
    line-height: 1;
    letter-spacing: 1px;
    color: var(--name-ink);
  }
  .brand-rule {
    display: block;
    margin: 44px auto 0;
    width: 400px;
    height: 4px;
  }
  .contact {
    position: absolute;
    left: 47px;
    top: 470px;
    margin: 0;
    font-size: 25px;
    line-height: 35px;
    color: var(--ink);
  }
  .contact strong {
    font-weight: 700;
  }
</style>
</head>
<body>
  <main class="card">
    <div class="wave-field" role="img" aria-label="Background pattern of light blue diagonal wavy lines on white"></div>

    <header class="brand">
      <h1 class="brand-name">The Paint Hut</h1>
      <svg class="brand-rule" viewBox="0 0 400 4" aria-hidden="true">
        <rect x="0" y="0" width="400" height="4" rx="2" fill="var(--rule)"/>
      </svg>
    </header>

    <p class="contact">
      <strong>THE PAINT HUT</strong> Hallorans Oar House The Reach. 17 Kellaby Rd.<br>
      Dunrook 2091 Sydney Mir Colbin 0437819025<br>
      miracolbin@mailnest.example <strong>Lorn Vesk</strong><br>
      0429573816<br>
      lvesk@harborlink.example
    </p>
  </main>
</body>
</html>
```